Need a fully working bigcommerce fashion apparel website

We are starting a bigcommerce fashion and apparel store. There we need a fully working bigcommerce website. The website themes should be good looking and attract more visitors. Please see the attachment for details.

Coding

Coded - Design and coding required

Font styles to use
Sans Serif

```html
<!DOCTYPE html>
<html lang="en">
<head>
<meta charset="utf-8">
<title>Linen Loom – Independent Brand Collective</title>
<link href="https://fonts.googleapis.com/css2?family=Lato:ital,wght@0,400;0,700;0,900;1,400&display=swap" rel="stylesheet">
<style>
:root{
  --blue:#1f9be8;
  --ink:#222;
  --line:#e2e2e2;
  --topbar:#ececec;
  --footer:#f2f2f2;
  --white:#fff;
}
*{box-sizing:border-box;margin:0;padding:0}
html,body{width:1200px;height:3921px;overflow:hidden}
body{font-family:'Lato',sans-serif;color:var(--ink);background:var(--white);position:relative}
.abs{position:absolute}
.photo{position:absolute}
.topbar{left:0;top:0;width:1200px;height:61px;background:var(--topbar);font-size:12px;font-weight:700;display:flex;align-items:center;justify-content:center;text-transform:uppercase}
.brand-mark{left:75px;top:88px;display:flex;align-items:center;gap:12px}
.brand-square{width:26px;height:26px;background:var(--ink)}
.brand-name{font-size:34px;font-weight:700;color:var(--ink);line-height:1}
.util{font-size:12px;color:var(--ink)}
.nav{left:0;top:160px;width:1200px;height:61px;border-top:1px solid var(--line);border-bottom:1px solid var(--line)}
.nav a{position:absolute;top:22px;font-size:14px;font-weight:700;color:var(--ink);text-decoration:none;transform:translateX(-50%);white-space:nowrap}
.nav a.active{color:var(--blue)}
.hero{left:75px;top:254px;width:1050px;height:485px;background:linear-gradient(100deg,#4f5a3c 0%,#8b8560 25%,#c8a592 48%,#d9b8a6 65%,#c9ab97 100%)}
.hero-title{left:75px;top:392px;width:1050px;text-align:center;font-size:68px;font-weight:900;color:#fff;line-height:1}
.hero-sub{left:75px;top:472px;width:1050px;text-align:center;font-size:38px;font-style:italic;color:#fff}
.btn{left:530px;top:544px;width:140px;height:44px;background:var(--blue);color:#fff;font-size:15px;font-weight:700;display:flex;align-items:center;justify-content:center}
.arrow{width:24px;height:40px}
.promo{top:766px;width:330px;height:258px}
.promo-text{position:absolute;left:14px;top:88px;color:#fff;line-height:1}
.promo-text .up{font-size:36px;font-weight:400;display:block}
.promo-text .pct{font-size:52px;font-weight:900}
.promo-text .off{font-size:26px;font-style:italic;font-weight:700}
.section-title{left:0;width:1200px;text-align:center;font-size:27px;font-weight:400;text-transform:uppercase}
.product-name{font-size:14px;font-weight:700}
.product-price{font-size:14px;font-weight:700}
.banner{left:75px;top:1476px;width:1050px;height:260px;background:radial-gradient(ellipse at 30% 90%,#0f74c4 0%,transparent 40%),radial-gradient(ellipse at 85% 80%,#1677c6 0%,transparent 35%),var(--blue)}
.banner-title{left:75px;top:1541px;width:1050px;text-align:center;font-size:49px;font-weight:700;color:#fff}
.banner-text{left:190px;top:1608px;width:820px;text-align:center;font-size:17px;line-height:28px;color:#fff}
.post-date{height:28px;padding:0 9px;background:var(--blue);color:#fff;font-size:13px;display:flex;align-items:center}
.post-title{font-size:19px;line-height:27px;color:var(--blue);width:330px}
.post-text{font-size:14px;line-height:26px;color:var(--ink);width:290px}
.brand{top:3197px;width:163px;height:93px;border:1px solid #ccc;display:flex;align-items:center;justify-content:center;font-size:22px;font-weight:700;color:var(--ink)}
.brand.dark{background:#aaa}
.footer{left:0;top:3351px;width:1200px;height:570px;background:var(--footer)}
.feat-icon{width:70px;height:70px;border:1px solid #bbb;border-radius:50%;display:flex;align-items:center;justify-content:center}
.feat-title{font-size:18px;color:var(--blue);text-transform:uppercase}
.feat-text{font-size:13px;line-height:20px;text-transform:uppercase}
.foot-head{top:3568px;font-size:17px;font-weight:700;text-transform:uppercase}
.foot-list{list-style:none;font-size:13px;line-height:34px}
.about{font-size:13px;line-height:26px;width:245px}
.rule{height:1px;background:#ddd}
.pay{font-size:12px;font-weight:700;color:#333}
.social{font-size:12px;font-weight:700;color:#333}
</style>
</head>
<body>

<div class="abs topbar">New offer this weekend only! Hurry shop now</div>

<header>
  <div class="abs brand-mark"><span class="brand-square"></span><span class="brand-name">Linen Loom</span></div>
  <div class="abs util" style="left:932px;top:89px">USD ⌄</div>
  <div class="abs util" style="left:997px;top:89px">|</div>
  <svg class="abs" style="left:1015px;top:90px" width="12" height="12" viewBox="0 0 12 12"><circle cx="5" cy="5" r="3.5" fill="none" stroke="#222" stroke-width="1.6"/><line x1="7.5" y1="7.5" x2="11" y2="11" stroke="#222" stroke-width="1.6"/></svg>
  <div class="abs util" style="left:1079px;top:89px">SEARCH</div>
  <div class="abs util" style="left:762px;top:127px">Shopping Bag</div>
  <div class="abs util" style="left:890px;top:127px">Gift Certificates</div>
  <div class="abs util" style="left:1031px;top:127px">Sign in &nbsp;Register</div>
</header>

<nav class="abs nav">
  <a class="active" style="left:260px">HOME</a>
  <a style="left:373px">BRANDS</a>
  <a style="left:535px">EXCLUSIVE BRANDS</a>
  <a style="left:739px">PRINT ON DEMAND</a>
  <a style="left:915px">CONTACT US</a>
</nav>

<section class="hero-block">
  <div class="photo hero" role="img" aria-label="Model in a pink belted dress beside tropical plants"></div>
  <div class="abs hero-title">LINEN LOOM</div>
  <div class="abs hero-sub">Independent Brand Collective</div>
  <div class="abs btn">SHOP NOW</div>
  <svg class="abs arrow" style="left:40px;top:477px" viewBox="0 0 24 40"><polyline points="18,4 4,20 18,36" fill="none" stroke="#333" stroke-width="2"/></svg>
  <svg class="abs arrow" style="left:1138px;top:477px" viewBox="0 0 24 40"><polyline points="6,4 20,20 6,36" fill="none" stroke="#333" stroke-width="2"/></svg>
</section>

<section class="promos">
  <div class="photo promo" style="left:75px;background:linear-gradient(90deg,#f8a91f 0%,#f8ae2b 55%,#e9d5c4 75%,#f5a71f 100%)" role="img" aria-label="Smiling woman with shopping bags"><div class="promo-text"><span class="up">UP TO</span><span class="pct">40 %</span> <span class="off">OFF</span></div></div>
  <div class="photo promo" style="left:434px;background:linear-gradient(90deg,#a8a8a8 0%,#b0b0b0 55%,#6b3434 75%,#a9a9a9 100%)" role="img" aria-label="Man in a burgundy blazer and sunglasses"><div class="promo-text"><span class="up">UP TO</span><span class="pct">10 %</span> <span class="off">OFF</span></div></div>
  <div class="photo promo" style="left:795px;background:linear-gradient(90deg,#3a1f1c 0%,#2a1716 50%,#e9e6e4 80%,#3a2220 100%)" role="img" aria-label="Two women in black and white outfits"><div class="promo-text"><span class="up">UP TO</span><span class="pct">40 %</span> <span class="off">OFF</span></div></div>
</section>

<section class="featured">
  <h2 class="abs section-title" style="top:1074px">Featured Products</h2>
  <div class="photo" style="left:135px;top:1165px;width:110px;height:175px;background:linear-gradient(#b39a98,#9e8888)" role="img" aria-label="Mauve sleeveless top"></div>
  <div class="photo" style="left:358px;top:1200px;width:215px;height:125px;background:linear-gradient(#d9766c,#c8625a)" role="img" aria-label="Coral cropped tee"></div>
  <div class="photo" style="left:702px;top:1155px;width:70px;height:190px;background:linear-gradient(90deg,#6d7a8f,#8c97a8,#6d7a8f)" role="img" aria-label="Checked trousers"></div>
  <div class="photo" style="left:932px;top:1165px;width:145px;height:165px;background:linear-gradient(#ece4dc,#d6cabd)" role="img" aria-label="Cream quilted backpack"></div>
  <div class="abs product-name" style="left:75px;top:1380px">Item 001 - Haversack</div>
  <div class="abs product-name" style="left:344px;top:1380px">Item 001 - Haversack</div>
  <div class="abs product-name" style="left:614px;top:1380px">Item 001 - Haversack</div>
  <div class="abs product-name" style="left:883px;top:1380px">Item 001 - Haversack</div>
  <div class="abs product-price" style="left:75px;top:1408px">$307.97</div>
  <div class="abs product-price" style="left:344px;top:1408px">$307.97</div>
  <div class="abs product-price" style="left:614px;top:1408px">$307.97</div>
  <div class="abs product-price" style="left:883px;top:1408px">$307.97</div>
</section>

<section class="shipping-banner">
  <div class="photo banner" role="img" aria-label="Blue watercolour texture"></div>
  <div class="abs banner-title">free SHIPPPING &amp; RETURN</div>
  <div class="abs banner-text">Lorem ipsum dolor sit amet, consectetur adipiscing elit. Nulla in auctor est. Vestibulum vel nunc quis turpis faucibus interdum ullamcorper non neque...</div>
</section>

<section class="arrivals">
  <h2 class="abs section-title" style="top:1794px">New Arrivals</h2>
  <div class="photo" style="left:160px;top:1870px;width:85px;height:200px;background:linear-gradient(90deg,#a4abb7,#c3c8d0,#a4abb7)" role="img" aria-label="Grey trousers"></div>
  <div class="photo" style="left:357px;top:1895px;width:212px;height:150px;background:linear-gradient(135deg,#c21a22,#7c0c12)" role="img" aria-label="Red patent high heel"></div>
  <div class="photo" style="left:662px;top:1865px;width:148px;height:210px;background:linear-gradient(#1c3f8a,#0f2a66)" role="img" aria-label="Navy polo shirt"></div>
  <div class="photo" style="left:870px;top:1852px;width:262px;height:180px;background:linear-gradient(#f2ac2a,#e59a1a)" role="img" aria-label="Yellow puffer jacket"></div>
  <div class="abs product-name" style="left:75px;top:2100px">Item 001 - Haversack</div>
  <div class="abs product-name" style="left:344px;top:2100px">Item 001 - Haversack</div>
  <div class="abs product-name" style="left:614px;top:2100px">Item 001 - Haversack</div>
  <div class="abs product-name" style="left:883px;top:2100px">Item 001 - Haversack</div>
  <div class="abs product-price" style="left:75px;top:2128px">$307.97</div>
  <div class="abs product-price" style="left:344px;top:2128px">$307.97</div>
  <div class="abs product-price" style="left:614px;top:2128px">$307.97</div>
  <div class="abs product-price" style="left:883px;top:2128px">$307.97</div>
</section>

<section class="lookbook">
  <div class="photo" style="left:75px;top:2202px;width:251px;height:171px;background:linear-gradient(120deg,#3b3b3b,#a7a7a7,#555)" role="img" aria-label="Woman leaning on a car in the city"></div>
  <div class="photo" style="left:341px;top:2202px;width:251px;height:171px;background:linear-gradient(90deg,#f6e9b8,#f3dfa8)" role="img" aria-label="Woman in retro sunglasses"></div>
  <div class="photo" style="left:608px;top:2202px;width:517px;height:171px;background:linear-gradient(100deg,#d8b48a,#c8a37c 45%,#eeeae4 75%,#f3f2ef)" role="img" aria-label="Trench coat, sunglasses and boots flat lay"></div>
  <div class="photo" style="left:75px;top:2390px;width:517px;height:170px;background:linear-gradient(100deg,#b49a86,#c58a78 40%,#c7b2a1 75%,#8c7b63)" role="img" aria-label="Woman in a red top sitting on a chair"></div>
  <div class="photo" style="left:608px;top:2390px;width:251px;height:170px;background:linear-gradient(90deg,#2d9ad6,#5f7fa0 40%,#e6d3d3 70%,#2d9ad6)" role="img" aria-label="Couple in sunglasses on blue background"></div>
  <div class="photo" style="left:874px;top:2390px;width:251px;height:170px;background:linear-gradient(90deg,#dcdcdc,#9a7a5a 55%,#dadada)" role="img" aria-label="Man swinging a camel coat"></div>
</section>

<section class="posts">
  <h2 class="abs section-title" style="top:2614px">Recent Posts</h2>
  <div class="photo" style="left:75px;top:2688px;width:331px;height:221px;background:linear-gradient(90deg,#e4d7c8,#b98c72 50%,#cdb9a2)" role="img" aria-label="Woman in a tan jumpsuit"></div>
  <div class="photo" style="left:434px;top:2688px;width:331px;height:221px;background:linear-gradient(135deg,#b48a62,#7a6a6e 45%,#8a4b33 80%)" role="img" aria-label="Hat, shirt, camera and shoes flat lay"></div>
  <div class="photo" style="left:794px;top:2688px;width:331px;height:221px;background:linear-gradient(90deg,#5a5a52,#3a3a34 45%,#a6a39a)" role="img" aria-label="Man in a dark jacket in a cafe"></div>
  <div class="abs post-date" style="left:85px;top:2863px">OCT 16, 2020</div>
  <div class="abs post-date" style="left:445px;top:2863px">OCT 16, 2020</div>
  <div class="abs post-date" style="left:804px;top:2863px">OCT 16, 2020</div>
  <div class="abs post-title" style="left:75px;top:2924px">Cras sollicitudin pellentesque metus pulvinar lacinia ipsum quia</div>
  <div class="abs post-title" style="left:435px;top:2924px">Cras sollicitudin pellentesque metus pulvinar lacinia ipsum quia</div>
  <div class="abs post-title" style="left:794px;top:2924px">Cras sollicitudin pellentesque metus pulvinar lacinia ipsum quia</div>
  <p class="abs post-text" style="left:75px;top:2986px">Donec fringilla, ipsum in scelerisque varius, lorem purus tempus est, eu convallis urna urna a arcu.</p>
  <p class="abs post-text" style="left:435px;top:2986px">Donec fringilla, ipsum in scelerisque varius, lorem purus tempus est, eu convallis urna urna a arcu.</p>
  <p class="abs post-text" style="left:794px;top:2986px">Donec fringilla, ipsum in scelerisque varius, lorem purus tempus est, eu convallis urna urna a arcu.</p>
</section>

<section class="brands">
  <h2 class="abs section-title" style="top:3150px;font-size:19px">Our Brands</h2>
  <svg class="abs" style="left:46px;top:3232px" width="14" height="24" viewBox="0 0 14 24"><polyline points="11,3 3,12 11,21" fill="none" stroke="#222" stroke-width="2.5"/></svg>
  <svg class="abs" style="left:1140px;top:3232px" width="14" height="24" viewBox="0 0 14 24"><polyline points="3,3 11,12 3,21" fill="none" stroke="#222" stroke-width="2.5"/></svg>
  <div class="abs brand" style="left:75px">Northbay</div>
  <div class="abs brand dark" style="left:253px">Halden</div>
  <div class="abs brand" style="left:431px">Ostrava</div>
  <div class="abs brand" style="left:607px;font-size:17px">Kettle Athletic</div>
  <div class="abs brand" style="left:785px">Marlowe</div>
  <div class="abs brand" style="left:963px">Vellani</div>
</section>

<footer>
  <div class="abs footer"></div>

  <div class="abs feat-icon" style="left:75px;top:3403px"><svg width="30" height="22" viewBox="0 0 30 22"><rect x="1" y="3" width="17" height="13" fill="#333"/><path d="M18 7h6l4 5v4H18z" fill="#333"/><circle cx="7" cy="18" r="3" fill="#333"/><circle cx="23" cy="18" r="3" fill="#333"/></svg></div>
  <div class="abs feat-title" style="left:165px;top:3407px">Free Shipping</div>
  <div class="abs feat-text" style="left:165px;top:3434px">Free shipping on order over $100</div>

  <div class="abs feat-icon" style="left:461px;top:3403px"><svg width="28" height="22" viewBox="0 0 28 22"><path d="M10 2 1 10l9 8v-5c8 0 13 2 17 8-1-9-6-14-17-15z" fill="#333"/></svg></div>
  <div class="abs feat-title" style="left:552px;top:3394px">Free Return</div>
  <div class="abs feat-text" style="left:552px;top:3421px;width:190px">Free return in 24h after purchasing</div>

  <div class="abs feat-icon" style="left:794px;top:3403px"><svg width="24" height="24" viewBox="0 0 24 24"><path d="M5 2l4 0 2 5-3 2c1 3 4 6 7 7l2-3 5 2v4c0 1-1 2-2 2C10 21 3 14 3 4c0-1 1-2 2-2z" fill="#333"/></svg></div>
  <div class="abs feat-title" style="left:884px;top:3407px">Call Toll Free</div>
  <div class="abs feat-text" style="left:884px;top:3434px">Call us 1-800-555-0142</div>

  <div class="abs rule" style="left:75px;top:3498px;width:1050px"></div>

  <div class="abs foot-head" style="left:75px">Navigate</div>
  <ul class="abs foot-list" style="left:75px;top:3597px"><li>About Us</li><li>Privacy Policy</li><li>Shipping &amp; Returns</li><li>Contact Us</li><li>Sitemap</li></ul>

  <div class="abs foot-head" style="left:302px">Categories</div>
  <ul class="abs foot-list" style="left:302px;top:3597px"><li>Independent Brands</li><li>Independent Suppliers</li><li>International Name Brands</li><li>Print On Demand</li><li>Uncategorized</li></ul>

  <div class="abs foot-head" style="left:589px">About Us</div>
  <p class="abs about" style="left:589px;top:3602px">Lorem ipsum dolor sit amet, inani persius inductum vim id, quo an nibh nusquam.<br>Cu movet discere cum, pri partem veritus comprehensam ea. Cum in liber movet simul. Nominavi volutpat an has, vim eripuit luptatum cu</p>

  <div class="abs foot-head" style="left:912px">Information</div>
  <div class="abs" style="left:912px;top:3609px;font-size:13px">♥</div>
  <div class="abs" style="left:946px;top:3605px;font-size:13px;line-height:20px;width:180px">Made With ♥ In Harbourtown, Westland</div>
  <svg class="abs" style="left:912px;top:3687px" width="14" height="10" viewBox="0 0 14 10"><rect width="14" height="10" fill="#333"/><polyline points="0,0 7,6 14,0" fill="none" stroke="#f2f2f2" stroke-width="1.2"/></svg>
  <div class="abs" style="left:946px;top:3682px;font-size:13px">hello@linenloom.example</div>
  <div class="abs foot-head" style="left:912px;top:3710px;font-size:16px">Connect Us</div>
  <div class="abs social" style="left:912px;top:3752px;display:flex;gap:12px"><span>Circle</span><span>Chirp</span><span>Frame</span><span>Network</span><span>Stream</span></div>

  <div class="abs rule" style="left:75px;top:3830px;width:1050px"></div>
  <div class="abs" style="left:75px;top:3862px;font-size:12px;line-height:24px">Copyright © 2020. Company Name<br>All Right Reserved</div>
  <div class="abs pay" style="left:855px;top:3875px;display:flex;gap:14px"><span>Centurion</span><span>Findcard</span><span>Orbit</span><span>Walletpay</span><span>Vistapay</span></div>
</footer>

</body>
</html>
```